update Coffeeshop menu design to be more modern and luxury

I want a menu that compliments the colors of the shop. I want a simple nice clean modern looking menu. The text is available on old menu (drinks) and the word document attached (food)

We changed the interior of our shop and want the new menu to reflect the new look and feel (see pictures attached). This project is a template menu therefore it should give us the ability to add content. Keep in mind that we want the layout to be one page . one side in english and the other in Arabic (we will update the arabic side to match the english design)
Updates

Project Deadline Extended
Reason: Now more information is provided including text and samples on old menu. The brand name is Brewvant.

Industry/Entity Type

Coffee Shop

Font styles to use
Sans Serif

Colors

Designer to choose colors to be used in the design.

Requirements
Must have
• My menu must have clean modern look that matches the shop style. It should have the logo of the coffee shop (provided). we would like a one pager menu one ideally (double sided) with variant in a3 and a4
• The design will be a template that we can update with content (content is not final). I attached the current menu for reference although content will be changed.
Nice to have
• Simple, attractive, easy to read, luxury modern.
Should not have
• Should not be crowded. no folds. no need for images. should not look like the old menu

```html
<!DOCTYPE html>
<html lang="en">
<head>
<meta charset="utf-8">
<title>Brewvant Menu</title>
<link rel="stylesheet" href="https://fonts.googleapis.com/css2?family=Montserrat:wght@500;600;700&family=Questrial&family=Noto+Kufi+Arabic:wght@400&display=swap">
<style>
  :root {
    --paper: #fdfbf6;
    --band: #f1ebdf;
    --gold: #c6a463;
    --gold-deep: #b38c4c;
    --gold-soft: #cfb27a;
    --price: #6a5838;
    --rule: #d9c49a;
  }
  * { margin: 0; padding: 0; box-sizing: border-box; }
  html, body { width: 849px; height: 1200px; overflow: hidden; background: var(--paper); }
  .menu { position: relative; width: 849px; height: 1200px; background: var(--paper); font-family: "Questrial", sans-serif; }
  .top-band { position: absolute; left: 0; top: 0; width: 849px; height: 26px; background: linear-gradient(var(--band), #f6f1e8); }
  .brand { position: absolute; top: 66px; left: 0; width: 849px; text-align: center; }
  .brand-name { font-family: "Montserrat", sans-serif; font-weight: 600; font-size: 48px; color: var(--gold); letter-spacing: 1px; line-height: 1; }
  .tagline { margin-top: 12px; font-family: "Montserrat", sans-serif; font-weight: 700; font-size: 12.5px; letter-spacing: 2.5px; color: var(--gold); }

  .section { position: absolute; width: 306px; }
  .section-title { text-align: center; font-family: "Montserrat", sans-serif; font-weight: 700; font-size: 16px; letter-spacing: 4px; color: var(--gold-deep); height: 20px; line-height: 20px; }
  .size-head { position: relative; height: 14px; border-bottom: 1px solid var(--rule); }
  .size-head span { position: absolute; bottom: 2px; width: 34px; text-align: center; font-family: "Montserrat", sans-serif; font-weight: 600; font-size: 6px; letter-spacing: .3px; color: var(--gold-deep); }
  .size-head .reg, .item .reg { left: 238px; }
  .size-head .lrg, .item .lrg { left: 278px; }
  .items { list-style: none; padding-top: 14px; }
  .item { position: relative; height: 22.8px; }
  .item-name { font-size: 10.5px; color: var(--gold-soft); text-transform: uppercase; line-height: 12px; white-space: nowrap; }
  .item-ar { font-family: "Noto Kufi Arabic", sans-serif; font-size: 6.5px; color: var(--gold-soft); line-height: 8px; direction: rtl; text-align: left; unicode-bidi: plaintext; }
  .price { position: absolute; top: 0; width: 34px; text-align: center; font-family: "Montserrat", sans-serif; font-weight: 700; font-size: 10.5px; color: var(--price); line-height: 12px; }
</style>
</head>
<body>
<main class="menu">
  <div class="top-band" role="img" aria-label="Decorative patterned border in soft cream tones"></div>

  <header class="brand">
    <div class="brand-name">Brewvant</div>
    <div class="tagline">COFFEE FOR ALL</div>
  </header>

  <!-- Left column -->
  <section class="section" style="left:71px; top:185px;">
    <h2 class="section-title">- HOT BEVERAGES -</h2>
    <div class="size-head"><span class="reg">REGULAR</span><span class="lrg">LARGE</span></div>
    <ul class="items">
      <li class="item"><div class="item-name">Espresso</div><div class="item-ar">إسبريسو</div><span class="price reg">11</span><span class="price lrg">13</span></li>
      <li class="item"><div class="item-name">Espresso con Panna</div><div class="item-ar">إسبريسو كون بانا</div><span class="price reg">14</span><span class="price lrg">16</span></li>
      <li class="item"><div class="item-name">Espresso Macchiato</div><div class="item-ar">إسبريسو ماكياتو</div><span class="price reg">13</span><span class="price lrg">15</span></li>
      <li class="item"><div class="item-name">Turkish Coffee</div><div class="item-ar">قهوة تركية</div><span class="price reg">11</span><span class="price lrg">13</span></li>
    </ul>
  </section>

  <section class="section" style="left:71px; top:329px;">
    <h2 class="section-title">- HOT COFFEE -</h2>
    <div class="size-head"><span class="reg">REGULAR</span><span class="lrg">LARGE</span></div>
    <ul class="items">
      <li class="item"><div class="item-name">Americano</div><span class="price reg">15</span><span class="price lrg">17</span></li>
      <li class="item"><div class="item-name">Cappucino</div><div class="item-ar">كابتشينو</div><span class="price reg">17</span><span class="price lrg">19</span></li>
      <li class="item"><div class="item-name">Café Latte</div><div class="item-ar">كافيه لاتيه</div><span class="price reg">17</span><span class="price lrg">19</span></li>
      <li class="item"><div class="item-name">Dark Mocha</div><div class="item-ar">موكا داكنة</div><span class="price reg">19</span><span class="price lrg">21</span></li>
      <li class="item"><div class="item-name">Caramel Macchiato</div><div class="item-ar">كراميل ماكياتو</div><span class="price reg">21</span><span class="price lrg">24</span></li>
      <li class="item"><div class="item-name">Hot Chocolate</div><div class="item-ar">شوكولاتة ساخنة</div><span class="price reg">19</span><span class="price lrg">21</span></li>
      <li class="item"><div class="item-name">Flat White</div><div class="item-ar">فلات وايت</div><span class="price reg">17</span></li>
      <li class="item"><div class="item-name">Arabic Coffee</div><div class="item-ar">قهوة عربية</div><span class="price reg">25</span></li>
      <li class="item"><div class="item-name">Hot Milk</div><div class="item-ar">حليب ساخن</div><span class="price reg">10</span></li>
      <li class="item"><div class="item-name">Tiramisu Latte</div><div class="item-ar">تيراميسو لاتيه</div><span class="price reg">19</span><span class="price lrg">21</span></li>
      <li class="item"><div class="item-name">Double Mocha</div><div class="item-ar">موكا مزدوجة</div><span class="price reg">19</span><span class="price lrg">21</span></li>
    </ul>
  </section>

  <section class="section" style="left:71px; top:628px;">
    <h2 class="section-title">- GOURMET TEA -</h2>
    <div class="size-head"></div>
    <ul class="items">
      <li class="item"><div class="item-name">English Breakfast Tea</div><div class="item-ar">شاي الإفطار الإنجليزي</div><span class="price reg">13</span></li>
      <li class="item"><div class="item-name">Earl Grey Tea</div><div class="item-ar">شاي إيرل جراي</div><span class="price reg">13</span></li>
      <li class="item"><div class="item-name">Peppermint Tea</div><div class="item-ar">شاي بالنعناع</div><span class="price reg">13</span></li>
      <li class="item"><div class="item-name">Camomille Tea</div><div class="item-ar">شاي البابونج</div><span class="price reg">13</span></li>
      <li class="item"><div class="item-name">Green Tea</div><div class="item-ar">شاي أخضر</div><span class="price reg">13</span></li>
      <li class="item"><div class="item-name">Chai Tea Latte</div><div class="item-ar">شاي لاتيه</div><span class="price reg">19</span><span class="price lrg">21</span></li>
    </ul>
  </section>

  <section class="section" style="left:85px; top:825px;">
    <h2 class="section-title">- ICED GOURMET TEA -</h2>
    <div class="size-head"><span class="reg">REGULAR</span><span class="lrg">LARGE</span></div>
    <ul class="items">
      <li class="item"><div class="item-name">Iced Green Tea</div><div class="item-ar">شاي أخضر مثلج</div><span class="price reg">15</span><span class="price lrg">117</span></li>
      <li class="item"><div class="item-name">Iced Green Tea with Honey Lemon</div><div class="item-ar">شاي أخضر مثلج بالعسل والليمون</div><span class="price reg">15</span><span class="price lrg">17</span></li>
      <li class="item"><div class="item-name">Iced Chamomile</div><div class="item-ar">بابونج مثلج</div><span class="price reg">15</span><span class="price lrg">17</span></li>
      <li class="item"><div class="item-name">Iced Cucumber Lemon Tea</div><div class="item-ar">شاي الخيار والليمون المثلج</div><span class="price reg">17</span><span class="price lrg">19</span></li>
      <li class="item"><div class="item-name">Iced Peach Tea</div><div class="item-ar">شاي الخوخ المثلج</div><span class="price reg">17</span><span class="price lrg">19</span></li>
      <li class="item"><div class="item-name">Iced Lemon Tea</div><div class="item-ar">شاي الليمون المثلج</div><span class="price reg">17</span><span class="price lrg">19</span></li>
    </ul>
  </section>

  <section class="section" style="left:71px; top:1019px;">
    <h2 class="section-title" style="width:340px; margin-left:-14px;">- JUICES AND FROSTIES -</h2>
    <div class="size-head"><span class="reg">REGULAR</span><span class="lrg">LARGE</span></div>
    <ul class="items">
      <li class="item"><div class="item-name">Citrus Frostie</div><div class="item-ar">فروستي الحمضيات</div><span class="price reg">17</span><span class="price lrg">19</span></li>
      <li class="item"><div class="item-name">Strawberry Frostie</div><div class="item-ar">فروستي الفراولة</div><span class="price reg">21</span><span class="price lrg">23</span></li>
      <li class="item"><div class="item-name">Lychee Frostie</div><div class="item-ar">فروستي الليتشي</div><span class="price reg">19</span><span class="price lrg">21</span></li>
      <li class="item"><div class="item-name">Orange Juice</div><div class="item-ar">عصير برتقال</div><span class="price reg">17</span><span class="price lrg">21</span></li>
      <li class="item"><div class="item-name">Lemon and Mint Juice</div><div class="item-ar">عصير الليمون بالنعناع</div><span class="price reg">13</span><span class="price lrg">15</span></li>
    </ul>
  </section>

  <!-- Right column -->
  <section class="section" style="left:456px; top:185px;">
    <h2 class="section-title">- FRAPPEVANT -</h2>
    <div class="size-head"><span class="reg">REGULAR</span><span class="lrg">LARGE</span></div>
    <ul class="items">
      <li class="item"><div class="item-name">Brewvant Frappevant</div><div class="item-ar">فرابيه بروفانت</div><span class="price reg">22</span><span class="price lrg">24</span></li>
      <li class="item"><div class="item-name">Dark Mocha Frappevant</div><div class="item-ar">فرابيه موكا داكنة</div><span class="price reg">20</span><span class="price lrg">22</span></li>
      <li class="item"><div class="item-name">Chocolate Frappevant</div><div class="item-ar">فرابيه شوكولاتة</div><span class="price reg">20</span><span class="price lrg">22</span></li>
      <li class="item"><div class="item-name">Vanilla Frappevant</div><div class="item-ar">فرابيه فانيلا</div><span class="price reg">20</span><span class="price lrg">22</span></li>
      <li class="item"><div class="item-name">Mango Frappevant</div><div class="item-ar">فرابيه مانجو</div><span class="price reg">20</span><span class="price lrg">22</span></li>
      <li class="item"><div class="item-name">Strawberry Frappevant</div><div class="item-ar">فرابيه فراولة</div><span class="price reg">21</span><span class="price lrg">23</span></li>
      <li class="item"><div class="item-name">Double Mocha Frappevant</div><div class="item-ar">فرابيه موكا مزدوجة</div><span class="price reg">20</span><span class="price lrg">22</span></li>
      <li class="item"><div class="item-name">Cookie and Cream Frappevant</div><div class="item-ar">فرابيه كوكيز وكريمة</div><span class="price reg">20</span><span class="price lrg">22</span></li>
      <li class="item"><div class="item-name">Coffee Crumble Frappevant</div><div class="item-ar">فرابيه كرمبل القهوة</div><span class="price reg">20</span><span class="price lrg">22</span></li>
    </ul>
  </section>

  <section class="section" style="left:456px; top:456px;">
    <h2 class="section-title">- COFFEE ON ICE -</h2>
    <div class="size-head"><span class="reg">REGULAR</span><span class="lrg">LARGE</span></div>
    <ul class="items">
      <li class="item"><div class="item-name">Iced Americano</div><div class="item-ar">أمريكانو مثلج</div><span class="price reg">17</span><span class="price lrg">19</span></li>
      <li class="item"><div class="item-name">Iced Cappucino</div><div class="item-ar">كابتشينو مثلج</div><span class="price reg">19</span><span class="price lrg">21</span></li>
      <li class="item"><div class="item-name">Iced Latte</div><div class="item-ar">لاتيه مثلج</div><span class="price reg">19</span><span class="price lrg">21</span></li>
      <li class="item"><div class="item-name">Iced Caramel Macchiato</div><div class="item-ar">كراميل ماكياتو مثلج</div><span class="price reg">19</span><span class="price lrg">21</span></li>
      <li class="item"><div class="item-name">Iced Mocha</div><div class="item-ar">موكا مثلجة</div><span class="price reg">19</span><span class="price lrg">21</span></li>
      <li class="item"><div class="item-name">Iced Chocolate</div><div class="item-ar">شوكولاتة مثلجة</div><span class="price reg">19</span><span class="price lrg">21</span></li>
      <li class="item"><div class="item-name">Iced Milk</div><div class="item-ar">حليب مثلج</div><span class="price reg">12</span></li>
      <li class="item"><div class="item-name">Iced Shaken Espresso</div><div class="item-ar">إسبريسو مخفوق مثلج</div><span class="price reg">17</span><span class="price lrg">19</span></li>
    </ul>
  </section>

  <section class="section" style="left:456px; top:705px;">
    <h2 class="section-title" style="width:340px; margin-left:-14px;">- ADDING VARIETY &amp; EXTRAS -</h2>
    <div class="size-head"><span class="reg">REGULAR</span><span class="lrg">LARGE</span></div>
    <ul class="items">
      <li class="item"><div class="item-name" style="text-transform:none;">ITALIAN SODA (Strawberry, Lychee, Lime)</div><div class="item-ar">صودا إيطالية</div><span class="price reg">17</span><span class="price lrg">19</span></li>
      <li class="item"><div class="item-name">Spring Water</div><div class="item-ar">مياه ينابيع</div><span class="price reg">10</span></li>
      <li class="item"><div class="item-name">Brewvant Water</div><div class="item-ar">مياه بروفانت</div><span class="price reg">5</span></li>
      <li class="item"><div class="item-name">Sparkling Water</div><div class="item-ar">مياه فوارة</div><span class="price reg">10</span></li>
      <li class="item"><div class="item-name">Extra Shot</div><div class="item-ar">جرعة إضافية</div><span class="price reg">4</span></li>
      <li class="item"><div class="item-name" style="text-transform:none;">SYRUP (Vanilla, Caramel, Hazelnut)</div><div class="item-ar">شراب منكه</div><span class="price reg">4</span></li>
      <li class="item"><div class="item-name">Whipped Cream</div><div class="item-ar">كريمة مخفوقة</div><span class="price reg">4</span></li>
      <li class="item"><div class="item-name">Chocolate Sauce</div><div class="item-ar">صوص شوكولاتة</div><span class="price reg">4</span></li>
      <li class="item"><div class="item-name">Caramel Sauce</div><div class="item-ar">صوص كراميل</div><span class="price reg">4</span></li>
      <li class="item"><div class="item-name">Almond Milk</div><div class="item-ar">حليب لوز</div><span class="price reg">4</span></li>
      <li class="item"><div class="item-name">Soya Milk</div><div class="item-ar">حليب صويا</div><span class="price reg">-</span></li>
    </ul>
  </section>

  <section class="section" style="left:456px; top:1019px;">
    <h2 class="section-title">- DESSERTS -</h2>
    <div class="size-head"><span class="reg">REGULAR</span><span class="lrg">LARGE</span></div>
    <ul class="items">
      <li class="item"><div class="item-name">Sandwiches</div><span class="price reg">-</span><span class="price lrg">-</span></li>
      <li class="item"><div class="item-name">Salads</div><div class="item-ar">سلطات</div><span class="price reg">-</span><span class="price lrg">-</span></li>
      <li class="item"><div class="item-name">Croissant</div><div class="item-ar">كرواسون</div><span class="price reg">-</span><span class="price lrg">-</span></li>
      <li class="item"><div class="item-name">Mufin &amp; Cookies</div><div class="item-ar">مافن وكوكيز</div><span class="price reg">-</span><span class="price lrg">-</span></li>
      <li class="item"><div class="item-name">Cakes</div><div class="item-ar">كيك</div><span class="price reg">-</span><span class="price lrg">-</span></li>
    </ul>
  </section>
</main>
</body>
</html>
```